A front Sign for The Harbourline Orthopaedic Centre

A sign for the front of our consulting rooms. Utilising logo winner of competition 3757477. Business card and letterhead competition 3793183. Specialist Orthopaedic surgeons. includes a phone number.

```html
<!DOCTYPE html>
<html lang="en">
<head>
<meta charset="utf-8">
<title>The Harbourline Orthopaedic Centre – Front Sign</title>
<link rel="stylesheet" href="https://fonts.googleapis.com/css2?family=Roboto:wght@400;500&display=swap">
<style>
  :root {
    --navy: #08314d;
    --sky: #53a9de;
    --white: #ffffff;
    --panel-top: #cdced3;
    --panel-bottom: #a8a9ae;
    --photo-light: #e6e6e8;
    --photo-mid: #c9c9cc;
    --xray-dark: #0c2433;
    --xray-light: #4f93b8;
    --backdrop: #6a6a6a;
  }
  * { margin: 0; padding: 0; box-sizing: border-box; }
  html, body {
    width: 1200px; height: 840px; overflow: hidden;
    background: var(--backdrop);
    font-family: "Roboto", Arial, sans-serif;
  }
  .sign {
    position: absolute; left: 50px; top: 98px;
    width: 1100px; height: 644px;
    background: var(--white);
    overflow: hidden;
  }
  .sign-shapes { position: absolute; inset: 0; width: 1100px; height: 644px; }
  .brand-name {
    position: absolute; left: 60px; top: 76px;
    font-size: 31px; font-weight: 400; color: var(--navy);
    white-space: nowrap; line-height: 1;
  }
  .phone {
    position: absolute; left: 640px; width: 460px; top: 46px;
    text-align: center; font-size: 56px; font-weight: 500;
    color: var(--white); line-height: 1; letter-spacing: 0.5px;
  }
  .services-heading {
    position: absolute; left: 57px; top: 161px;
    font-size: 42px; font-weight: 400; color: var(--navy); line-height: 1;
  }
  .services-list {
    position: absolute; left: 57px; top: 222px;
    list-style: none; color: var(--navy);
    font-size: 25px; line-height: 46.3px;
  }
  .website {
    position: absolute; left: 640px; width: 424px; top: 587px;
    text-align: center; font-size: 29px; font-weight: 500;
    color: var(--navy); line-height: 1;
  }
</style>
</head>
<body>
  <div class="sign">
    <svg class="sign-shapes" viewBox="0 0 1100 644" aria-hidden="false">
      <defs>
        <linearGradient id="panel-fade" x1="0" y1="0" x2="0" y2="1">
          <stop offset="0" stop-color="var(--panel-top)"/>
          <stop offset="1" stop-color="var(--panel-bottom)"/>
        </linearGradient>
        <linearGradient id="photo-fade" x1="0" y1="0" x2="1" y2="1">
          <stop offset="0" stop-color="var(--photo-light)"/>
          <stop offset="1" stop-color="var(--photo-mid)"/>
        </linearGradient>
        <linearGradient id="xray-fade" x1="0" y1="1" x2="1" y2="0">
          <stop offset="0" stop-color="var(--xray-dark)"/>
          <stop offset="1" stop-color="var(--xray-light)"/>
        </linearGradient>
      </defs>
      <!-- header band -->
      <polygon class="phone-band" points="673,0 1100,0 1100,132 606,132" fill="var(--navy)"/>
      <!-- services panel -->
      <rect class="services-panel" x="0" y="132" width="1100" height="416" fill="url(#panel-fade)"/>
      <polygon class="services-marker" points="0,168 53,168 39,195 0,195" fill="var(--navy)"/>
      <!-- diagonal stripes -->
      <polygon class="stripe-sky" points="561,132 582,132 360,548 338,548" fill="var(--sky)"/>
      <polygon class="stripe-navy" points="582,132 603,132 383,548 360,548" fill="var(--navy)"/>
      <!-- image areas -->
      <polygon class="specialist-photo" role="img" aria-label="Portrait photograph of a smiling orthopaedic specialist in a white coat"
               points="603,132 843,132 634,548 383,548" fill="url(#photo-fade)"/>
      <polygon class="knee-xray" role="img" aria-label="Blue-toned X-ray of a knee with a joint replacement implant"
               points="843,132 1100,132 1100,548 634,548" fill="url(#xray-fade)"/>
      <!-- footer band -->
      <polygon class="footer-band" points="0,566 604,566 563,644 0,644" fill="var(--sky)"/>
    </svg>

    <div class="brand-name">The Harbourline Orthopaedic Centre</div>
    <div class="phone">(123) 555-0187</div>

    <h2 class="services-heading">Services</h2>
    <ul class="services-list">
      <li>Orthopedic Care</li>
      <li>Sports Medicine</li>
      <li>Concussion</li>
      <li>Pain Management</li>
      <li>Physical Medicine</li>
      <li>Rheumatology</li>
      <li>and more...</li>
    </ul>

    <div class="website">www.harbourlineortho.com</div>
  </div>
</body>
</html>
```